Business Card cabinets and cabinets components making company.

the card should be formal and interesting at the same time. The main colors will be black and white.

Font styles to use
Sans Serif

Colors

Designer to choose only greyscale colors for use in the design.

Requirements
Must have
• At least must have the followings:
office phone
cell phone
address
position
name
email
web

```html
<!DOCTYPE html>
<html lang="en">
<head>
<meta charset="utf-8">
<title>Trim Line – Business Card</title>
<link rel="stylesheet" href="https://fonts.googleapis.com/css2?family=Mulish:wght@400;700&display=swap">
<style>
  :root {
    --page-bg: #e4e2df;
    --card-light: #f2f2f4;
    --card-dark: #3a3a3c;
    --ink: #3a3a3c;
    --ink-soft: #4a4a4c;
    --rule: #6a6a6c;
    --paper: #ffffff;
  }
  * { box-sizing: border-box; margin: 0; padding: 0; }
  html, body {
    width: 1131px; height: 1200px; overflow: hidden;
    background: var(--page-bg);
    font-family: "Mulish", sans-serif;
  }
  .canvas { position: relative; width: 1131px; height: 1200px; }

  .card {
    position: absolute; left: 213px; width: 780px; height: 448px;
    box-shadow: 0 14px 24px rgba(0,0,0,0.18);
  }
  .card--front { top: 56px; background: var(--card-light); color: var(--ink); }
  .card--back { top: 600px; background: var(--card-dark); color: var(--paper); }

  .brand {
    display: flex; align-items: center; gap: 14px;
    font-weight: 700; letter-spacing: 0.5px;
  }
  .brand__square { display: block; background: currentColor; }

  .card--front .brand {
    position: absolute; left: 70px; top: 196px;
    font-size: 40px; color: var(--ink);
  }
  .card--front .brand__square { width: 22px; height: 22px; }

  .divider {
    position: absolute; left: 382px; top: 105px;
    width: 2px; height: 238px; background: var(--rule);
  }

  .details { position: absolute; left: 450px; top: 92px; }
  .details__name { font-size: 32px; font-weight: 400; line-height: 1.1; }
  .details__role { font-size: 18px; line-height: 1.3; color: var(--ink-soft); }
  .details__address {
    margin-top: 16px; font-size: 16px; line-height: 22px;
    font-style: normal; color: var(--ink-soft);
  }
  .contacts { list-style: none; margin-top: 10px; font-size: 16px; color: var(--ink-soft); }
  .contacts li { display: flex; align-items: center; gap: 10px; height: 22px; }
  .contacts svg { width: 13px; height: 13px; fill: var(--ink); flex: none; }

  .card--back .brand {
    position: absolute; left: 0; right: 0; top: 160px;
    justify-content: center; font-size: 76px;
  }
  .card--back .brand__square { width: 30px; height: 30px; }
  .card--back .web {
    position: absolute; left: 0; right: 0; top: 398px;
    text-align: center; font-size: 17px; letter-spacing: 0.3px;
  }
</style>
</head>
<body>
<main class="canvas">
  <section class="card card--front" aria-label="Card front">
    <div class="brand"><span class="brand__square"></span><span>Trim Line</span></div>
    <div class="divider"></div>
    <div class="details">
      <h1 class="details__name">Dana Whitcombe</h1>
      <p class="details__role">president</p>
      <address class="details__address">48 West 31st Street,<br>7th FL New York,<br>NY 10001</address>
      <ul class="contacts">
        <li>
          <svg viewBox="0 0 16 16" aria-hidden="true"><path d="M3.5 1.5l2.5 3-1.5 1.6c.8 2 2.4 3.6 4.4 4.4L10.5 9l3 2.5-1.3 2.6C6.8 13.8 2.2 9.2 1.9 3z"/></svg>
          <span>(212) 555-0147</span>
        </li>
        <li>
          <svg viewBox="0 0 16 16" aria-hidden="true"><path d="M1 6c0-2 3.5-3 7-3s7 1 7 3v1.5h-3.5V6h-7v1.5H1z"/><path d="M3.5 8h9l1 6h-11zM8 9.5a1.8 1.8 0 100 3.6 1.8 1.8 0 000-3.6z"/></svg>
          <span>(212) 555-0182</span>
        </li>
        <li>
          <svg viewBox="0 0 16 16" aria-hidden="true"><path d="M1 3.5h14v9H1z M2 4.5l6 4.5 6-4.5" stroke="#f2f2f4" stroke-width="1"/></svg>
          <span>dana@trimlinecabinets.net</span>
        </li>
        <li>
          <svg viewBox="0 0 16 16" aria-hidden="true"><circle cx="8" cy="8" r="7"/><path d="M1 8h14M8 1c-3 3.5-3 10.5 0 14M8 1c3 3.5 3 10.5 0 14" stroke="#f2f2f4" stroke-width="1" fill="none"/></svg>
          <span>www.trimlinecabinets.com</span>
        </li>
      </ul>
    </div>
  </section>

  <section class="card card--back" aria-label="Card back">
    <div class="brand"><span class="brand__square"></span><span>Trim Line</span></div>
    <p class="web">www.trimlinejoinery.com</p>
  </section>
</main>
</body>
</html>
```